Gestaltung einer Webseite für Eventfotografie
quirlmoos hat hervorragende Arbeit geleistet. Das Design ist 1A, sowie die weitere Projektabwicklung, völlig problemlos, sehr freundlich, entgegenkommend und kompetent. Ich kann quirlmoos jederzeit mit 5 Sternen als Designer weiterempfehlen! gernold
Zielgruppe
Eventagenturen, Entscheider in Marketing- bzw. Eventabteilungen von mittelständischen oder großen Firmen sowie Bankettabteilungen von Hotels.
Aufgabenstellung
Neuerstellung Webseitenlayout und programmtechnische Umsetzung einer Webseite.
Die Webseite soll "Das Glanzstück"heissen. Die Wörter "Das Glanzstück" wären grafisch dementsprechend auch zu gestalten.
Die Webseite dient als Schaufenster zur Generierung von Anfragen / Aufträgen die Eventfotografie betreffend. Da der erste Eindruck entscheidend ist, stelle ich mir beim Aufruf der Webseite vor, dass prominent 3-5 Fotos erscheinen. Die Animation der Fotos soll so gestaltet sein, als wenn man Papierabzüge auf einen Tisch legt (Mein Haus, Mein Pferd, mein Boot...)
Darüber hinaus sollen weitere weniger auffällige Eventfotos erscheinen.
Es sollen eine Homepage, eine Kontaktseite, eine Fotogalerieseite, eine Referenzseite (mit Kundennamen und Fotos) und evtl. ein Onlinekalender integriert sein, auf dem der Benutzer das Eventdatum anklicken und seine Anfrage platzieren kann. Impressum ist obligatorisch.
Alle Bereiche sollen übersichtlich und klar gestaltet sein, so dass sich der User schnell orientieren kann.
Auf jeder Unterseite soll ein ca. 5DM-Stück grosser auffälliger "Termin-Anfrage"-Button platziert sein.

```html
<!DOCTYPE html>
<html lang="de">
<head>
<meta charset="utf-8">
<title>Das Glanzstück – Eventfotografie</title>
<link href="https://fonts.googleapis.com/css2?family=Montserrat:wght@200;400&display=swap" rel="stylesheet">
<style>
  :root {
    --bg: #000;
    --bg-glow: #2a2a2a;
    --band: #1b335f;
    --band-edge: #0d1a30;
    --text: #f2f2f2;
    --nav: #4b80e6;
    --cta: #b31f2a;
    --cta-dark: #5c0c12;
  }
  html, body { margin: 0; padding: 0; overflow: hidden; background: var(--bg); }
  .page {
    position: relative; width: 1200px; height: 903px; overflow: hidden;
    background:
      radial-gradient(ellipse 700px 300px at 25% 10%, var(--bg-glow), transparent 70%),
      radial-gradient(ellipse 600px 250px at 85% 95%, #222, transparent 70%),
      var(--bg);
    font-family: "Montserrat", sans-serif;
  }
  .brand {
    position: absolute; right: 40px; top: 176px; margin: 0;
    font-weight: 200; font-size: 58px; letter-spacing: 2px;
    color: var(--text); text-transform: uppercase;
  }
  .photo-strip {
    position: absolute; left: 187px; top: 303px; width: 852px; height: 161px;
    background: linear-gradient(90deg, #3a3a3a 0%, #cfcfcf 12%, #555 30%, #9a9a9a 48%, #2e2e2e 62%, #8c8c8c 78%, #1e1e1e 100%);
  }
  .welcome {
    position: absolute; left: 21px; top: 499px; width: 1160px; height: 168px;
    background: var(--band);
  }
  .welcome::before, .welcome::after {
    content: ""; position: absolute; top: 0; width: 29px; height: 100%; background: var(--band-edge);
  }
  .welcome::before { left: 60px; }
  .welcome::after { right: 59px; }
  .welcome p {
    position: absolute; left: 165px; top: 12px; width: 880px; margin: 0;
    color: var(--text); font-size: 12.5px; line-height: 32px; letter-spacing: 1.6px;
    text-transform: uppercase;
  }
  .welcome .rule {
    position: absolute; left: 162px; top: 152px; width: 423px;
    border-top: 1px dotted #b8c2d8;
  }
  .cta {
    position: absolute; left: 619px; top: 604px; width: 168px; height: 168px;
    border-radius: 50%;
    background: radial-gradient(circle at 50% 35%, var(--cta) 55%, var(--cta-dark) 100%);
    color: #fff; text-align: center; text-decoration: none;
    display: flex; flex-direction: column; justify-content: center;
  }
  .cta .big { font-size: 36px; line-height: 40px; }
  .cta .small { font-size: 22px; line-height: 28px; }
  .main-nav {
    position: absolute; left: 0; width: 1200px; top: 816px; text-align: center;
    font-size: 17px; letter-spacing: 1.4px; color: var(--nav);
  }
  .main-nav a { color: var(--nav); text-decoration: none; }
  .main-nav .sep { margin: 0 6px; }
</style>
</head>
<body>
<div class="page">
  <h1 class="brand">Das Glanzstück</h1>

  <div class="photo-strip" role="img" aria-label="Schwarzweiß-Panorama von Eventfotos: Lounge mit Bildergalerie, Messestand mit Publikum, Fahrzeugpräsentation"></div>

  <section class="welcome">
    <p>Willkommen bei Das Glanzstück, der Agentur für Ihre perfekten Bilder und Fotos !<br>
    Ihre Veranstaltung ist unser Ansporn das beste Ergebnis für Sie zu erzielen, ohne<br>
    das Sie tief in die Geldbörse greifen müssen, denn Das Glanzstück bietet Ihnen sehr<br>
    günstige Konditionen und das dauerhaft !</p>
    <div class="rule"></div>
  </section>

  <a class="cta" href="#anfrage">
    <span class="big">Jetzt</span>
    <span class="small">Terminanfrage</span>
    <span class="small" style="font-size:27px;line-height:34px">stellen !</span>
  </a>

  <nav class="main-nav">
    <a href="#">HOME</a><span class="sep">|</span><a href="#">PORTRAIT</a><span class="sep">|</span><a href="#">GALERIE</a><span class="sep">|</span><a href="#">REFERENZEN</a><span class="sep">|</span><a href="#">HONORAR</a><span class="sep">|</span><a href="#">ANFRAGE</a><span class="sep">|</span><a href="#">KONTAKT</a><span class="sep">|</span><a href="#">IMPRESSUM</a>
  </nav>
</div>
</body>
</html>
```